NEW Brand "New Zealand Wine Estate"

We are looking for a design for our new range of New Zealand wine. An estate label that can be used for several varietals.
We have three potential names...
Hollow Pine Estate
Amber Lantern Estate
Morvina Estate
first variant is "Central Otago Pinot Noir" please use this in the original design.
This brand is for world export, so will need to be appealing to many markets but representative of New Zealand and our rugged Coasts.
Target Market(s)
Supermarket $25 NZD per bottle price point. Young and hip
Font styles to use
Decorative
Script
Requirements
Must have
- Sophistication but edgy. Stand out on a shelf.
- the brand needs to be able to be used for red or white wine.

```html
<!DOCTYPE html>
<html lang="en">
<head>
<meta charset="utf-8">
<title>Hollow Pine Estate – Label Range</title>
<link href="https://fonts.googleapis.com/css2?family=Cinzel:wght@400;500&family=Pinyon+Script&display=swap" rel="stylesheet">
<style>
  :root {
    --backdrop: #a8a8a8;
    --label-dark: #1c1c1d;
    --label-light: #c9c6be;
    --ink-light: #f1efe9;
    --ink-dark: #2b2b2b;
    --accent-red: #9e2b30;
    --accent-green: #1e6b3a;
    --coast-deep: #1f3a55;
    --coast-mid: #3d5d80;
    --coast-water: #6f7fc4;
    --coast-glow: #d8c9a6;
  }
  * { margin: 0; padding: 0; box-sizing: border-box; }
  html, body {
    width: 801px; height: 1200px; overflow: hidden;
    background: var(--backdrop);
  }
  .range {
    position: relative; width: 801px; height: 1200px;
    display: flex; justify-content: center; align-items: center; gap: 40px;
  }
  .label {
    position: relative; width: 310px; height: 380px;
    display: flex; flex-direction: column; align-items: center;
    box-shadow: 0 6px 18px rgba(0,0,0,.25);
  }
  .label--red { background: var(--label-dark); color: var(--ink-light); }
  .label--white { background: var(--label-light); color: var(--ink-dark); }
  .label__mark {
    width: 48px; height: 48px; margin-top: 20px;
    border: 2px solid rgba(255,255,255,.8);
  }
  .label--red .label__mark { background: var(--accent-red); }
  .label--white .label__mark { background: var(--accent-green); }
  .label__estate {
    margin-top: 22px;
    font-family: 'Cinzel', serif; font-size: 13px; letter-spacing: .04em;
  }
  .label__origin {
    margin-top: 4px;
    font-family: 'Pinyon Script', cursive; font-size: 15px;
  }
  .label--red .label__origin { color: var(--accent-red); }
  .label--white .label__origin { color: var(--accent-green); }
  .label__region {
    margin-top: 30px;
    font-family: 'Cinzel', serif; font-size: 12px; letter-spacing: .03em;
  }
  .label__varietal {
    margin-top: 6px;
    font-family: 'Cinzel', serif; font-size: 19px; letter-spacing: .02em;
  }
  .label__coast {
    position: absolute; left: 0; bottom: 0; width: 100%; height: 128px;
    background:
      linear-gradient(180deg, transparent 0%, transparent 45%, var(--coast-glow) 46%, var(--coast-water) 58%, var(--coast-mid) 100%) center / 30% 100% no-repeat,
      linear-gradient(180deg, var(--coast-mid) 0%, var(--coast-deep) 100%);
  }
</style>
</head>
<body>
<main class="range">
  <section class="label label--red">
    <div class="label__mark"></div>
    <p class="label__estate">Hollow Pine Estate</p>
    <p class="label__origin">New Zealand</p>
    <p class="label__region">Central Otago</p>
    <p class="label__varietal">Pinot Noir</p>
    <div class="label__coast" role="img" aria-label="Illustration of rugged blue coastal cliffs framing a calm bay at dusk"></div>
  </section>
  <section class="label label--white">
    <div class="label__mark"></div>
    <p class="label__estate">Hollow Pine Estate</p>
    <p class="label__origin">New Zealand</p>
    <p class="label__region">Central Otago</p>
    <p class="label__varietal">Pinot Grigio</p>
    <div class="label__coast" role="img" aria-label="Illustration of rugged blue coastal cliffs framing a calm bay at dusk"></div>
  </section>
</main>
</body>
</html>
```